Financial Planning business needs a new Business Card design

We need a business card design for an Australian financial planning business. I am looking for a clean simple design

Target Market(s)

People aged 25-40

Industry/Entity Type

Financial Service

Contact Information for Business Card

On the front of the card we need the following information:
Name: Derek Holloway (First Name Green: #006838 and last name Grey: #414042)
Position: Financial Adviser
Qualifications: BEc(Hons), AdDipFS(FP), Dip FMBM, AFP®
Mobile: 0437 215 604
Email: derek@mondlane.com.au

On the back of the card we need:
Postal address: PO BOX 5736, PERTH BC, WA 6849
Website: www.mondlane.com.au
Text: AFS Licence No. 518624

The fields need to be able to be edited.

Font styles to use
Sans Serif

Requirements
Must have
• Information listed above

```html
<!DOCTYPE html>
<html lang="en">
<head>
<meta charset="utf-8">
<title>Mondlane Business Card</title>
<link href="https://fonts.googleapis.com/css2?family=Lato:wght@400;700;900&display=swap" rel="stylesheet">
<style>
  :root {
    --brand-green: #006838;
    --card-green: #1b6e3f;
    --brand-grey: #414042;
    --ink: #1e1e1e;
    --paper: #ffffff;
    --backdrop: #e6e6e4;
  }
  * { box-sizing: border-box; margin: 0; padding: 0; }
  html, body { width: 1200px; height: 900px; overflow: hidden; }
  body {
    background: var(--backdrop);
    font-family: "Lato", sans-serif;
    position: relative;
  }
  .card {
    position: absolute;
    left: 250px;
    width: 700px;
    height: 400px;
    overflow: hidden;
    box-shadow: 0 6px 18px rgba(0,0,0,0.18);
  }
  /* Back side */
  .card-back {
    top: 35px;
    background: var(--card-green);
    color: var(--paper);
  }
  .card-back .wordmark {
    position: absolute;
    top: 138px;
    left: 0;
    width: 100%;
    text-align: center;
    font-weight: 900;
    font-size: 76px;
    letter-spacing: 2px;
    color: var(--paper);
  }
  .card-back .footer-line {
    position: absolute;
    bottom: 42px;
    left: 0;
    width: 100%;
    text-align: center;
    font-size: 19px;
    letter-spacing: 1px;
  }
  /* Front side */
  .card-front {
    top: 465px;
    background: var(--paper);
    color: var(--ink);
  }
  .card-front .wordmark {
    position: absolute;
    top: 34px;
    right: 46px;
    font-weight: 900;
    font-size: 54px;
    line-height: 1;
    letter-spacing: 2px;
    color: var(--brand-green);
  }
  .identity { position: absolute; top: 44px; left: 44px; }
  .identity .name { font-size: 30px; line-height: 1.2; color: var(--brand-grey); font-weight: 400; }
  .identity .name .first { color: var(--brand-green); }
  .identity .position { font-size: 19px; line-height: 1.2; color: var(--brand-grey); margin-top: 6px; }
  .identity .qualifications { font-size: 17px; line-height: 1.2; color: var(--brand-grey); margin-top: 4px; white-space: nowrap; }
  .divider {
    position: absolute;
    top: 160px;
    left: 40px;
    right: 40px;
    height: 1px;
    background: var(--brand-grey);
  }
  .contact { position: absolute; top: 194px; left: 44px; list-style: none; }
  .contact li { display: flex; align-items: center; gap: 12px; font-size: 20px; margin-bottom: 8px; }
  .contact svg { width: 16px; height: 16px; fill: var(--brand-green); }
  .address {
    position: absolute;
    right: 46px;
    top: 214px;
    text-align: right;
    font-size: 24px;
    line-height: 1.25;
    font-style: normal;
    color: var(--ink);
  }
  .base-band { position: absolute; left: 0; bottom: 0; width: 700px; height: 80px; }
</style>
</head>
<body>

<section class="card card-back" aria-label="Card back">
  <div class="wordmark">MONDLANE</div>
  <p class="footer-line">www.mondlane.com.au • AFS Licence No. 518624</p>
</section>

<section class="card card-front" aria-label="Card front">
  <div class="wordmark">MONDLANE</div>
  <div class="identity">
    <h1 class="name"><span class="first">Derek</span> Holloway</h1>
    <p class="position">Financial Adviser</p>
    <p class="qualifications">BEc(Hons), AdDipFS(FP), Dip FMBM, AFP®</p>
  </div>
  <div class="divider"></div>
  <ul class="contact">
    <li>
      <svg viewBox="0 0 16 16"><rect x="4" y="0" width="8" height="16" rx="1.5"/><rect x="5.5" y="2" width="5" height="9" fill="#fff"/></svg>
      0437 215 604
    </li>
    <li>
      <svg viewBox="0 0 16 16"><rect x="0" y="3" width="16" height="11"/><polyline points="0.5,3.5 8,9.5 15.5,3.5" fill="none" stroke="#fff" stroke-width="1.3"/></svg>
      derek@mondlane.com.au
    </li>
  </ul>
  <address class="address">PO BOX 5736,<br>PERTH BC, WA 6849</address>
  <svg class="base-band" viewBox="0 0 700 80" aria-hidden="true">
    <polygon points="0,12 360,12 384,40 700,40 700,80 0,80" fill="var(--brand-green)"/>
    <polygon points="0,0 345,0 372,26 0,26" fill="var(--brand-grey)"/>
  </svg>
</section>

</body>
</html>
```